Professional & attention grabbing.

A business card design, front and back. I already have a logo I will attach, but I am open to something new as well.
Things to include:
Name:
Title:
Phone:
Email:
Wanting something that is professional but attention grabbing.
Also we do a lot of work using drones on natural gas pipelines (leading the future)if you want to include any of that. I'm open to ideas.
Target Market(s)
Natural gas transmission industry / greenhouse gas mitigation industry
Industry/Entity Type
Business
Contact Information for Business Card
All details have been conveyed above.
Colors
Designer to choose colors to be used in the design.
Look and feel
Each slider illustrates characteristics of the customer's brand and the style your logo design should communicate.

```html
<!DOCTYPE html>
<html lang="en">
<head>
<meta charset="utf-8">
<title>KV Field Inspections — Business Card</title>
<link rel="stylesheet" href="https://fonts.googleapis.com/css2?family=Open+Sans:wght@400;600;700;800&display=swap">
<style>
  :root {
    --canvas-bg: #ecebe8;
    --card-white: #ffffff;
    --charcoal: #3a3a3c;
    --brand-red: #be1e24;
    --text-light: #ffffff;
  }
  * { margin: 0; padding: 0; box-sizing: border-box; }
  html, body {
    width: 1200px; height: 900px; overflow: hidden;
    background: var(--canvas-bg);
    font-family: "Open Sans", Arial, sans-serif;
  }
  .canvas { position: relative; width: 1200px; height: 900px; }

  .card { position: absolute; box-shadow: 0 10px 28px rgba(0,0,0,.18); }

  /* Front */
  .card-front {
    left: 78px; top: 34px; width: 587px; height: 364px;
    display: flex;
  }
  .brand-panel {
    width: 285px; height: 100%;
    background: linear-gradient(160deg, var(--brand-red) 0%, var(--brand-red) 38%, var(--card-white) 38%, var(--card-white) 62%, var(--charcoal) 62%, var(--charcoal) 100%);
  }
  .info-panel {
    flex: 1; background: var(--charcoal); color: var(--text-light);
    text-align: right; padding: 44px 37px 0 0;
    display: flex; flex-direction: column; align-items: flex-end;
  }
  .company-name {
    font-weight: 800; font-size: 38px; line-height: 1.05;
    letter-spacing: .5px; text-transform: uppercase; color: var(--text-light);
  }
  .person { margin-top: 56px; }
  .person-name { font-weight: 700; font-size: 19px; letter-spacing: .3px; }
  .person-title { font-size: 15px; margin-top: 1px; }
  .contact { margin-top: 26px; font-size: 15px; line-height: 23px; }
  .contact-line { display: flex; align-items: center; justify-content: flex-end; gap: 8px; }
  .contact-line svg { width: 13px; height: 13px; fill: var(--text-light); }

  /* Back */
  .card-back {
    left: 388px; top: 505px; width: 567px; height: 352px;
    background: var(--card-white);
    display: flex; align-items: center; justify-content: center;
  }
  .lockup { display: flex; align-items: center; gap: 14px; }
  .lockup-mark { width: 34px; height: 34px; background: var(--brand-red); }
  .lockup-name {
    font-weight: 800; font-size: 30px; line-height: 1.05;
    text-transform: uppercase; color: var(--charcoal); letter-spacing: .4px;
  }
</style>
</head>
<body>
<main class="canvas">
  <section class="card card-front">
    <div class="brand-panel" role="img" aria-label="Brand colour panel in red, white and charcoal"></div>
    <div class="info-panel">
      <p class="company-name">KV Field<br>Inspections</p>
      <div class="person">
        <p class="person-name">DANIEL WARD</p>
        <p class="person-title">Managing Director</p>
      </div>
      <div class="contact">
        <p class="contact-line">(044)987650321
          <svg viewBox="0 0 24 24" aria-hidden="true"><path d="M6.6 10.8a15.1 15.1 0 0 0 6.6 6.6l2.2-2.2a1 1 0 0 1 1-.25 11.4 11.4 0 0 0 3.6.57 1 1 0 0 1 1 1V20a1 1 0 0 1-1 1A17 17 0 0 1 3 4a1 1 0 0 1 1-1h3.5a1 1 0 0 1 1 1c0 1.25.2 2.45.57 3.57a1 1 0 0 1-.25 1z"/></svg>
        </p>
        <p class="contact-line">hello@kvfield.com
          <svg viewBox="0 0 24 24" aria-hidden="true"><path d="M2 5h20v14H2z M3.5 6.5 12 13l8.5-6.5" fill="none" stroke="#fff" stroke-width="0"/><path d="M2 5h20v1.2L12 13 2 6.2z"/><path d="M2 8l10 7 10-7v11H2z"/></svg>
        </p>
      </div>
    </div>
  </section>

  <section class="card card-back">
    <div class="lockup">
      <span class="lockup-mark" aria-hidden="true"></span>
      <p class="lockup-name">KV Field<br>Inspections</p>
    </div>
  </section>
</main>
</body>
</html>
```